First North America Product Category Rule

8 x 10 foot booth design for a stretch fabric wrap-around. The booth will be used in a very small exhibit area for 150 attendees. It is for the packaging industry focused on the environment. This booth graphic is NOT about our company, but to promote participation in a project we are sponsoring. The project is to develop the first North American Packaging Category Rule, so the booth is to invite conference attendees to join our effort. Production specifications are attached.

Target Market(s)

Meridian 300, Sustainability Directors, Packaging Engineers

Industry/Entity Type

Packaging; Environment

Font styles to use
Sans Serif

Requirements
Must have
• An Eye-Catching or Intriguing Image/Graphics/Letter Treatment
Should not have
• Nothing too bright or garish. All text should be above waist height (No text below the 36-40" mark)

```html
<!DOCTYPE html>
<html lang="en">
<head>
<meta charset="utf-8">
<title>First North American PCR for Protective Packaging – Booth Graphic</title>
<link rel="stylesheet" href="https://fonts.googleapis.com/css2?family=Montserrat:wght@500;600;700;800&family=Oswald:wght@600;700&family=Rubik:wght@500;700;800&display=swap">
<style>
  :root {
    --orange: #ec7a1f;
    --green: #5aac44;
    --blue: #0aa8d6;
    --slate: #5a6270;
    --ink: #1d1d1d;
    --white: #ffffff;
  }
  html, body {
    margin: 0;
    width: 910px;
    height: 1200px;
    overflow: hidden;
    background: var(--white);
  }
  h1, h2, p { margin: 0; }
  .stage {
    position: absolute;
    left: 25px;
    top: 357px;
    width: 860px;
    height: 486px;
    box-shadow: 6px 10px 18px rgba(0,0,0,0.35);
    overflow: hidden;
  }
  .booth {
    position: absolute;
    left: 0;
    top: 0;
    width: 1312px;
    height: 742px;
    transform: scale(0.6555);
    transform-origin: 0 0;
    font-family: "Montserrat", sans-serif;
  }
  .booth-shapes { position: absolute; inset: 0; }
  .headline-tag {
    position: absolute;
    left: 220px; top: 43px;
    width: 413px; height: 47px;
    display: flex; align-items: center; justify-content: center;
    font-family: "Oswald", sans-serif;
    font-style: italic;
    font-weight: 700;
    font-size: 27px;
    line-height: 1;
    white-space: nowrap;
    color: var(--white);
  }
  .title {
    position: absolute;
    left: 190px; top: 100px;
    width: 470px;
    text-align: center;
    font-family: "Rubik", sans-serif;
    font-size: 24px;
    line-height: 34px;
    white-space: nowrap;
  }
  .title-lead { color: var(--blue); font-weight: 500; font-size: 24px; display: block; }
  .title-main { color: var(--orange); font-weight: 800; font-size: 27px; display: block; }
  .quote-text {
    position: absolute;
    left: 216px; top: 240px;
    width: 399px;
    text-align: center;
    font-weight: 600;
    font-size: 16px;
    line-height: 22px;
    white-space: nowrap;
    color: var(--ink);
  }
  .leaf-label {
    position: absolute;
    width: 90px;
    text-align: center;
    font-weight: 700;
    font-size: 9px;
    line-height: 12px;
    white-space: nowrap;
    color: var(--white);
  }
  .leaf-num {
    position: absolute;
    font-weight: 700;
    font-size: 16px;
    line-height: 20px;
    color: var(--white);
  }
  .sponsor {
    position: absolute;
    right: 729px; top: 622px;
    text-align: right;
    font-size: 17px;
    line-height: 24px;
    white-space: nowrap;
    color: var(--white);
    font-weight: 500;
  }
  .sponsor strong { font-weight: 700; }
  .cta {
    position: absolute;
    left: 388px; top: 675px;
    width: 200px; height: 37px;
    display: flex; align-items: center; justify-content: center;
    font-family: "Oswald", sans-serif;
    font-weight: 700;
    font-size: 27px;
    line-height: 1;
    white-space: nowrap;
    color: var(--white);
  }
</style>
</head>
<body>
<main class="stage">
  <section class="booth">
    <svg class="booth-shapes" viewBox="0 0 1312 742" width="1312" height="742">
      <defs>
        <linearGradient id="panelShade" x1="0" y1="0" x2="1" y2="1">
          <stop offset="0" stop-color="#ececec"/>
          <stop offset="0.5" stop-color="#fafafa"/>
          <stop offset="1" stop-color="#e6e6e6"/>
        </linearGradient>
        <linearGradient id="warehouseTone" x1="0" y1="0" x2="1" y2="1">
          <stop offset="0" stop-color="#6b6f82"/>
          <stop offset="0.45" stop-color="#c8b98a"/>
          <stop offset="0.75" stop-color="#d9dc6a"/>
          <stop offset="1" stop-color="#8c8f96"/>
        </linearGradient>
      </defs>
      <rect class="base-orange" width="1312" height="742" fill="var(--orange)"/>
      <polygon class="light-panel" points="143,20 845,20 615,610 0,610 0,380" fill="url(#panelShade)"/>
      <polygon class="blue-field" points="853,0 1312,0 1312,742 560,742" fill="var(--blue)"/>
      <polygon class="green-corner" points="1312,10 1312,150 1275,150" fill="var(--green)"/>
      <polygon class="photo-area" points="823,150 1312,150 1312,400 1228,742 597,742" fill="url(#warehouseTone)" role="img" aria-label="Photo of a smiling warehouse worker in a high-visibility vest holding a blue hard hat and a tablet"/>
      <polygon class="orange-corner" points="1312,400 1312,742 1228,742" fill="var(--orange)"/>
      <polygon class="green-footer" points="0,610 648,608 598,742 0,742" fill="var(--green)"/>
      <polygon class="orange-stripe" points="618,608 648,608 598,742 565,742" fill="var(--orange)"/>
      <polygon class="headline-band" points="228,43 635,43 625,90 218,90" fill="var(--green)"/>
      <path class="quote-frame" d="M270,226 H608 a7,7 0 0 1 7,7 V333 a7,7 0 0 1 -7,7 H592 M556,340 H223 a7,7 0 0 1 -7,-7 V233 a7,7 0 0 1 7,-7 H238" fill="none" stroke="var(--green)" stroke-width="1.5"/>
      <text x="241" y="252" font-family="Oswald, sans-serif" font-weight="700" font-size="46" fill="var(--green)">&#8220;</text>
      <text x="558" y="370" font-family="Oswald, sans-serif" font-weight="700" font-size="46" fill="var(--green)">&#8221;</text>
      <g class="process-clover" stroke="#e2e2e2" stroke-width="5">
        <path d="M391,468 V417 A51,51 0 0 0 340,366 A51,51 0 0 0 289,417 A51,51 0 0 0 340,468 Z" fill="var(--green)"/>
        <path d="M395,468 V417 A51,51 0 0 1 446,366 A51,51 0 0 1 497,417 A51,51 0 0 1 446,468 Z" fill="var(--orange)"/>
        <path d="M391,472 V523 A51,51 0 0 1 340,574 A51,51 0 0 1 289,523 A51,51 0 0 1 340,472 Z" fill="var(--slate)"/>
        <path d="M395,472 V523 A51,51 0 0 0 446,574 A51,51 0 0 0 497,523 A51,51 0 0 0 446,472 Z" fill="var(--blue)"/>
      </g>
      <polygon class="cta-band" points="396,675 590,675 580,712 386,712" fill="var(--blue)"/>
    </svg>

    <h2 class="headline-tag">Enlisting Stakeholder Participation</h2>
    <h1 class="title">
      <span class="title-lead">First North American</span>
      <span class="title-main">Product Category Rule (PCR)</span>
      <span class="title-main">For Protective Packaging</span>
    </h1>
    <p class="quote-text">How EPD Can Move the Dialogue Beyond<br>End-of-Life Disposal to Include<br>Environmental Benchmarks for Product<br>Production &amp; Distribution</p>

    <span class="leaf-label" style="left:297px;top:394px">PCR<br>Product Category<br>Rules</span>
    <span class="leaf-label" style="left:401px;top:394px">LCA<br>Life Cycle<br>Assessment</span>
    <span class="leaf-label" style="left:297px;top:508px">EPD<br>Registration and<br>Publication</span>
    <span class="leaf-label" style="left:401px;top:508px">Third<br>Party<br>Verification</span>
    <span class="leaf-num" style="left:367px;top:442px">01</span>
    <span class="leaf-num" style="left:400px;top:442px">02</span>
    <span class="leaf-num" style="left:367px;top:476px">04</span>
    <span class="leaf-num" style="left:400px;top:476px">03</span>

    <p class="sponsor">Sponsored by <strong>Foam Packaging Council Managed<br>by Clear Ledger Group</strong></p>
    <span class="cta">SIGN UP NOW!</span>
  </section>
</main>
</body>
</html>
```